Korvane Sky Works, LLC - Business Card

I currently have a drone business that specializes in aerial photography, thermal image inspections, deer recovery, search and rescue, custom agricultural applications. i will attach my current business card as well as some logos to incorporate for a new up to date business card
Updates

Designs look the same

Sick

Target Market(s)

farmers, hunters

Contact Information for Business Card

name address phone number (as existing card i attached)

Requirements
Must have
• im good with existing business card, but would like an agricultural twist

```html
<!DOCTYPE html>
<html lang="en">
<head>
<meta charset="utf-8">
<title>Korvane Sky Works, LLC – Business Card</title>
<link rel="stylesheet" href="https://fonts.googleapis.com/css2?family=Roboto+Condensed:wght@300;400;700&display=swap">
<style>
  :root {
    --bg: #3a3a3c;
    --green-light: #5fa52a;
    --green-mid: #3f8a1c;
    --green-dark: #1f6d10;
    --white: #ffffff;
    --curve-grey: #6b6b6b;
    --text-font: "Roboto Condensed", sans-serif;
  }
  * { margin: 0; padding: 0; box-sizing: border-box; }
  html, body { width: 1200px; height: 689px; overflow: hidden; }
  body {
    background: var(--bg);
    font-family: var(--text-font);
    position: relative;
  }
  .card {
    position: absolute;
    top: 195px;
    width: 525px;
    height: 300px;
    border-radius: 18px;
    overflow: hidden;
  }
  /* Front side */
  .card-front {
    left: 45px;
    background: radial-gradient(circle at 50% 35%, var(--green-light), var(--green-mid) 55%, var(--green-dark));
    color: var(--white);
  }
  .brand-mark {
    position: absolute;
    top: 62px;
    left: 0; right: 0;
    display: flex;
    flex-direction: column;
    align-items: center;
    gap: 10px;
  }
  .brand-ring {
    width: 58px; height: 58px;
    border: 5px solid var(--white);
    border-radius: 50%;
  }
  .brand-name {
    font-size: 30px;
    font-weight: 700;
    letter-spacing: 2px;
    text-transform: uppercase;
  }
  .rule {
    position: absolute;
    left: 28px; right: 28px;
    height: 1px;
    background: rgba(255,255,255,0.85);
  }
  .rule-top { top: 186px; }
  .rule-bottom { bottom: 28px; }
  .services {
    position: absolute;
    top: 198px;
    left: 0; right: 0;
    text-align: center;
    font-size: 15px;
    font-weight: 400;
    line-height: 20px;
    letter-spacing: 0.3px;
    text-transform: uppercase;
  }
  .services .sep {
    display: inline-block;
    width: 8px; height: 8px;
    margin: 0 8px 2px;
    background: var(--white);
    border-radius: 0 8px 0 8px;
  }
  /* Back side */
  .card-back {
    left: 630px;
    background: var(--white);
  }
  .back-shape {
    position: absolute;
    inset: 0;
  }
  .logo-lockup {
    position: absolute;
    left: 30px;
    top: 78px;
    width: 170px;
    display: flex;
    flex-direction: column;
    align-items: center;
    gap: 10px;
    color: var(--green-mid);
  }
  .logo-ring {
    width: 62px; height: 62px;
    border: 5px solid var(--green-mid);
    border-radius: 50%;
  }
  .logo-name {
    font-size: 30px;
    font-weight: 700;
    letter-spacing: 1.5px;
    text-transform: uppercase;
  }
  .contact {
    position: absolute;
    right: 26px;
    top: 34px;
    text-align: right;
    color: var(--white);
  }
  .person-name {
    font-size: 24px;
    font-weight: 300;
    text-transform: uppercase;
    letter-spacing: 0.5px;
    line-height: 1;
  }
  .person-name strong { font-weight: 700; }
  .person-role {
    font-size: 13px;
    font-weight: 300;
    margin-top: 3px;
  }
  .address {
    margin-top: 30px;
    font-size: 14px;
    line-height: 18px;
  }
  .details {
    margin-top: 12px;
    list-style: none;
    font-size: 14px;
    line-height: 19px;
  }
  .details li {
    display: flex;
    justify-content: flex-end;
    align-items: center;
    gap: 8px;
  }
  .details svg { width: 12px; height: 12px; fill: var(--white); }
  .details .noicon { padding-right: 20px; }
</style>
</head>
<body>

<section class="card card-front" aria-label="Front of business card">
  <div class="brand-mark">
    <span class="brand-ring"></span>
    <span class="brand-name">Korvane</span>
  </div>
  <div class="rule rule-top"></div>
  <p class="services">
    Thermal Image Inspections<span class="sep"></span>Deer Recovery<br>
    Search &amp; Rescue<span class="sep"></span>Real Estate Photography
  </p>
  <div class="rule rule-bottom"></div>
</section>

<section class="card card-back" aria-label="Back of business card">
  <svg class="back-shape" viewBox="0 0 525 300" preserveAspectRatio="none" aria-hidden="true">
    <defs>
      <radialGradient id="panelGreen" cx="0.6" cy="0.4" r="0.8">
        <stop offset="0" stop-color="#5fa52a"/>
        <stop offset="0.6" stop-color="#3f8a1c"/>
        <stop offset="1" stop-color="#1f6d10"/>
      </radialGradient>
    </defs>
    <path d="M300 0 C 238 70, 238 230, 300 300 L 306 300 C 250 230, 250 70, 312 0 Z" fill="var(--curve-grey)"/>
    <path d="M316 0 C 254 70, 254 230, 316 300 L 525 300 L 525 0 Z" fill="url(#panelGreen)"/>
  </svg>

  <div class="logo-lockup">
    <span class="logo-ring"></span>
    <span class="logo-name">Korvane</span>
  </div>

  <div class="contact">
    <h1 class="person-name">Marcus <strong>Hale</strong></h1>
    <p class="person-role">Owner</p>
    <p class="address">214 N. Elm St.<br>Brandt, OH 45190</p>
    <ul class="details">
      <li>419-555-0142
        <svg viewBox="0 0 24 24" aria-hidden="true"><path d="M6.6 10.8a15.1 15.1 0 006.6 6.6l2.2-2.2a1 1 0 011-.25 11.4 11.4 0 003.6.57 1 1 0 011 1V20a1 1 0 01-1 1A17 17 0 013 4a1 1 0 011-1h3.5a1 1 0 011 1c0 1.25.2 2.45.57 3.6a1 1 0 01-.25 1z"/></svg>
      </li>
      <li>korvanesky@mail.com
        <svg viewBox="0 0 24 24" aria-hidden="true"><path d="M2 5h20v14H2z M2 5l10 8 10-8" fill="none" stroke="#fff" stroke-width="2.5"/></svg>
      </li>
      <li>www.korvaneskyworks.com
        <svg viewBox="0 0 24 24" aria-hidden="true"><circle cx="12" cy="12" r="10" fill="none" stroke="#fff" stroke-width="2.5"/><path d="M2 12h20M12 2c3 3 3 17 0 20M12 2c-3 3-3 17 0 20" fill="none" stroke="#fff" stroke-width="2"/></svg>
      </li>
    </ul>
  </div>
</section>

</body>
</html>
```